Fashion-Doll Website

I'm looking to create a new and better website for my growing fashion-doll brand, MARLOW.

About me: I'm a Eastbrook-based artist, illustrator, and doll-maker and MARLOW is the name of my doll. Marlow is a character doll (one girl) but she's not necessarily defined by any particular physical trait outside of the sculpt of the doll and her unique sense of style. For example, she could have pink hair and freckles or dark skin and green eyes, but she would still be "Marlow."

My partner and I created the current website ourselves using Adobe Muse. While it has served its purpose, we are not professional graphic or web designers, so I'm looking to graduate to a much more sophisticated and streamlined web design. I want the site to feel sweet and homespun but also hip and edgy. Because the site is so image heavy, I think black and white or black and off-white might be the best color palate, but I'm open to seeing other palates. Marlow's signature color is a muted lavender so maybe that could be integrated into the design. Here is the link:

www.MarlowFigure.com

I want the website to feel more like a shop and less like a gallery/info page. I'm now selling one-of-a-kind porcelain dolls, limited-edition resin dolls, face-plate necklaces, paper dolls, custom doll services, and printed Marlow throw pillows. I also need an interface that will allow me to create new categories, update inventory, and post new items easily.

I need to add new sections for press/articles, multiple image galleries (photography, products, illustrations, comics, and fan art), **collaboration projects, and several flash based doll "dress-up" games.

I would prefer a design that I can code/update myself using Adobe Muse. PSD files import into Muse, so I would prefer that you use them. I'm certainly not opposed to other designs, but I would prefer a design I can manage myself.

I'm including some photos and drawings of Marlow that express her look and vibe. I don't want to use these images in the web design necessarily (I think simple is best) but I thought they would be helpful in expressing the kind of girl she is and how I want the site to feel. I want to work with someone who has a clean, refined, yet whimsical aesthetic who can help me create a website that really expresses how special Marlow is.

Reason: I have had a family emergency come up and I can't devote time to this right now so I'm extending the deadline another 10 days.

Target Market(s)

young eccentrics, art collectors, fashion enthusiasts, and adult doll-collectors

Industry/Entity Type

Fashion

Requirements
Must have
• I need the following main categories: Info, Sales, Galleries, Press, and Dress-up. However, I don't necessarily want or expect the layout to be organized like the current website.

INFO:

*About Marlow (the character)

*Doll specifications: 27" porcelain doll, 22" porcelain doll, 22" resin doll, life-size doll (for window display)

*About the artist

SALES:

*Porcelain dolls

*Resin dolls

*Face-plate necklaces

*Pillows

*Custom doll/necklace info and inquiry form

GALLERIES:

*Photographs

*Collaboration projects

*Illustrations/Comics

*Fan Art/Contests

PRESS:

*An inventory of pdf's of articles about Marlow for users to download or view inside a reader online.

DRESS UP:

*Links to two interactive flash based dress-up games (interactive paper dolls)

Nice to have
• I hold online drawing and design contests from time to time so I would love to have a spot on the site reserved to host the rules and results of my contests.

Marlow has a large facebook and Instagram following so links to her social media would also be great.
instagram: @marlowfigure
facebook: facebook.com/marlowfigure

Should not have
• I'm not looking to see anything too girly, too young, or too sexy.
Marlow is not Tessa, Meadow Child, or Zoomi. She's a sophisticated young girl who is fresh, funky, and free-spirited.

```html
<!DOCTYPE html>
<html lang="en">
<head>
<meta charset="utf-8">
<title>Marlow — Fashion Doll</title>
<link rel="stylesheet" href="https://fonts.googleapis.com/css2?family=Delius&family=PT+Sans:wght@400;700&family=Tinos:wght@400;700&display=swap">
<style>
  :root {
    --salmon: #f5a38a;
    --salmon-deep: #ef8f74;
    --rose-band: #e85f75;
    --ink: #2b2b2b;
    --paper: #ffffff;
    --mist: #efeeee;
    --bar-grey: #e6e6e6;
    --frame-cream: #e4dfca;
    --thumb-edge: #e8dca0;
  }
  * { box-sizing: border-box; margin: 0; padding: 0; }
  html, body { width: 1084px; height: 1200px; overflow: hidden; background: var(--paper); }
  .site {
    position: relative; width: 1000px; height: 1107px;
    transform: scale(1.084); transform-origin: 0 0;
    font-family: "PT Sans", sans-serif; color: var(--ink);
  }
  .abs { position: absolute; }

  .top-rule { left: 0; top: 0; width: 1000px; height: 5px; background: var(--salmon); }
  .brand { left: 176px; top: 14px; font-family: "Delius", cursive; font-size: 34px; color: var(--ink); letter-spacing: 1px; line-height: 1; }
  .nav { left: 547px; top: 5px; display: flex; height: 50px; font-family: "Tinos", serif; font-weight: 700; font-size: 9.5px; }
  .nav a { color: var(--salmon); text-decoration: none; padding: 0 11px; line-height: 50px; }
  .nav a.is-current { background: var(--salmon); color: var(--paper); padding: 0 10px; }

  .band { left: 0; top: 63px; width: 1000px; height: 42px; background: var(--rose-band); }

  .hero {
    left: 164px; top: 65px; width: 671px; height: 287px;
    border: 3px solid var(--frame-cream);
    box-shadow: 0 22px 28px -14px rgba(0,0,0,.22);
    background:
      radial-gradient(ellipse 260px 220px at 560px 150px, #d9a7a3 0%, #b87780 35%, rgba(60,40,52,0) 75%),
      linear-gradient(90deg, #1d1a21 0%, #27222b 45%, #3a2c35 100%);
  }
  .hero-copy { left: 182px; top: 113px; width: 178px; text-align: center; font-family: "Delius", cursive; font-size: 7.8px; line-height: 1.32; color: var(--salmon); }
  .hero-copy .name { font-size: 26px; float: left; line-height: 1; margin: -2px 3px 0 4px; }
  .btn {
    background: var(--salmon); color: var(--paper); border-radius: 8px;
    box-shadow: 1px 2px 3px rgba(0,0,0,.25); text-align: center;
  }
  .hero-btn { left: 227px; top: 241px; width: 106px; height: 26px; line-height: 26px; font-family: "Delius", cursive; font-size: 10px; }

  .bio { left: 165px; top: 395px; width: 670px; height: 58px; background: var(--mist); padding: 9px 56px 0; text-align: center; font-family: "Tinos", serif; font-size: 10.6px; line-height: 12px; color: var(--salmon); }

  .carousel-arrow { top: 516px; }
  .thumb { top: 472px; width: 102px; height: 125px; border: 1px solid var(--thumb-edge); }

  .card { top: 620px; width: 213px; height: 177px; border: 1px solid var(--salmon); }
  .card-icon { position: absolute; left: 5px; top: 8px; }
  .card-title { position: absolute; left: 42px; top: 14px; font-size: 12.5px; font-weight: 700; color: var(--salmon); line-height: 17px; letter-spacing: .3px; }
  .card-text { position: absolute; left: 8px; top: 57px; width: 200px; font-size: 8.2px; line-height: 13px; color: var(--ink); }
  .card-btn { position: absolute; left: 114px; top: 145px; width: 86px; height: 25px; line-height: 25px; font-size: 9px; font-weight: 700; letter-spacing: .4px; }

  .field-label { position: absolute; font-size: 8px; color: var(--ink); }
  .field { position: absolute; left: 34px; width: 160px; height: 22px; border: 1.5px dashed var(--salmon); border-radius: 3px; }
  .submit-btn { position: absolute; left: 74px; top: 120px; width: 86px; height: 26px; line-height: 26px; font-size: 9px; font-weight: 700; }

  .section-title { left: 168px; top: 820px; font-size: 14px; font-weight: 700; color: var(--salmon); letter-spacing: .3px; }
  .section-bar { left: 257px; top: 823px; width: 576px; height: 14px; background: var(--bar-grey); }

  .product { top: 859px; width: 154px; height: 155px; border: 1px dashed #cfcfcf; }
  .product-tag { position: absolute; right: 6px; top: 12px; writing-mode: vertical-rl; font-family: "Delius", cursive; font-size: 10px; letter-spacing: 5px; color: #e05a8a; }
  .product-name { top: 1019px; width: 154px; text-align: center; font-family: "Tinos", serif; font-weight: 700; font-size: 9px; color: var(--salmon); }

  .footer { left: 0; top: 1050px; width: 1000px; height: 57px; background: var(--salmon); }
  .footer-title { left: 0; top: 1058px; width: 975px; text-align: center; font-size: 9px; font-weight: 700; color: var(--paper); }
  .social { top: 1075px; width: 22px; height: 22px; border-radius: 3px; }
</style>
</head>
<body>
<div class="site">
  <div class="abs top-rule"></div>
  <div class="abs brand">MARLOW</div>
  <nav class="abs nav">
    <a class="is-current" href="#">Marlow</a>
    <a href="#">Info</a>
    <a href="#">Sales</a>
    <a href="#">Galleries</a>
    <a href="#">Press</a>
    <a href="#">Dress-up</a>
  </nav>

  <div class="abs band"></div>
  <div class="abs hero" role="img" aria-label="Close portrait photograph of the porcelain doll with pink hair and white flowers"></div>
  <p class="abs hero-copy"><span class="name">Marlow</span> is a free-spirited city girl. An art lover and fashion enthusiast, she spends her time sketching or at the sewing machine. Marlow draws inspiration from high and low, old and new: haute couture, street style, vintage and modern. Whether in a simple day-dress, an embellished hoop skirt, or dressed for an elaborate costume gala, Marlow projects a style uniquely her own.</p>
  <div class="abs btn hero-btn">View more</div>

  <p class="abs bio">Julian Reed Mercer is an Eastbrook-based artist, illustrator, and doll-maker. Originally from Millford, OH, Julian moved to the city in 2003 to become a professional illustrator. After years of creating two-dimensional art, Julian began experimenting with sculpture, mold-making, casting, and eventually porcelain—a progression that naturally led him to dolls, a life-long fascination</p>

  <svg class="abs carousel-arrow" style="left:166px" width="26" height="38" viewBox="0 0 26 38"><path d="M22 3 L6 19 L22 35" fill="none" stroke="var(--salmon)" stroke-width="7"/></svg>
  <svg class="abs carousel-arrow" style="left:808px" width="26" height="38" viewBox="0 0 26 38"><path d="M4 3 L20 19 L4 35" fill="none" stroke="var(--salmon)" stroke-width="7"/></svg>
  <div class="abs thumb" style="left:221px;background:linear-gradient(#cfd6d8,#a9a08f 55%,#d45a7a)" role="img" aria-label="Photograph of the doll in sunglasses and pink shorts by the sea"></div>
  <div class="abs thumb" style="left:332px;background:linear-gradient(#4b5a6a,#3b4a63 50%,#2d5a8a)" role="img" aria-label="Photograph of the doll with dark hair in a blue patterned top"></div>
  <div class="abs thumb" style="left:446px;background:linear-gradient(#3e4a2f,#d9d2c8 55%,#c0303a)" role="img" aria-label="Photograph of the doll in a white blouse and red trousers outdoors"></div>
  <div class="abs thumb" style="left:558px;background:linear-gradient(#f3e6e2,#efdcd8 60%,#c94040)" role="img" aria-label="Photograph of the pale porcelain doll in a red polka-dot dress"></div>
  <div class="abs thumb" style="left:669px;background:linear-gradient(#3d4a2a,#6b6a4a 55%,#8a8a7a)" role="img" aria-label="Photograph of the doll in a white dress sitting among plants"></div>

  <section class="abs card" style="left:164px">
    <svg class="card-icon" width="34" height="34" viewBox="0 0 34 34"><g fill="var(--salmon)"><circle cx="17" cy="17" r="11"/><g stroke="var(--salmon)" stroke-width="5"><line x1="17" y1="2" x2="17" y2="32"/><line x1="2" y1="17" x2="32" y2="17"/><line x1="6.4" y1="6.4" x2="27.6" y2="27.6"/><line x1="27.6" y1="6.4" x2="6.4" y2="27.6"/></g></g><circle cx="17" cy="17" r="5" fill="#fff"/></svg>
    <h3 class="card-title">Check out Photographs</h3>
    <p class="card-text">Maecenas ipsum metus, semper hendrerit varius mattis, congue sit amet tellus. Aliquam ullamcorper dui sed magna posue re ut elementum enim rutrum. Nam mi erat, porta id ultrices nec, pellentesque vel nunc. Cras varius fermentum iaculis. Aenean sodales nibh non lectus tempor a interdum justo ultricies.</p>
    <div class="btn card-btn">READ MORE</div>
  </section>

  <section class="abs card" style="left:393px">
    <svg class="card-icon" width="34" height="34" viewBox="0 0 34 34"><g fill="var(--salmon)"><circle cx="17" cy="11" r="8"/><path d="M3 33 Q3 19 17 19 Q31 19 31 33 Z"/></g></svg>
    <h3 class="card-title" style="left:48px">Follow Us on Chirpline,<br>Facepage</h3>
    <p class="card-text">Maecenas ipsum metus, semper hendrerit varius mattis, congue sit amet tellus. Aliquam ullamcorper dui sed magna posue re ut elementum enim rutrum. Nam mi erat, porta id ultrices nec, pellentesque vel nunc. Cras varius fermentum iaculis. Aenean sodales nibh non lectus tempor a interdum justo ultricies.</p>
    <div class="btn card-btn">READ MORE</div>
  </section>

  <section class="abs card" style="left:620px">
    <svg class="card-icon" width="38" height="34" viewBox="0 0 38 34"><path d="M4 17 L14 28 L34 6" fill="none" stroke="var(--salmon)" stroke-width="8" stroke-linejoin="miter"/></svg>
    <h3 class="card-title" style="left:50px">Newsletter Sign Up</h3>
    <span class="field-label" style="left:6px;top:66px">Name</span>
    <div class="field" style="top:59px"></div>
    <span class="field-label" style="left:6px;top:97px">E.mail</span>
    <div class="field" style="top:91px"></div>
    <div class="btn submit-btn">SUBMIT</div>
  </section>

  <h2 class="abs section-title">AVAILABLE</h2>
  <div class="abs section-bar"></div>

  <div class="abs product" style="left:166px;background:linear-gradient(#2a2420,#4a3a30 50%,#e8d8e0)" role="img" aria-label="Photograph of the doll with a voluminous dark afro and a frilled white blouse"></div>
  <div class="abs product" style="left:337px;background:linear-gradient(#2a1426,#3a1a30 55%,#2a1424)" role="img" aria-label="Photograph of a porcelain pendant on a gold chain">
    <span class="product-tag">NEW ARRIVAL</span>
  </div>
  <div class="abs product" style="left:508px;background:linear-gradient(#eee8e4,#e4d2d0 55%,#d9c8c4)" role="img" aria-label="Photograph of the pale-haired doll wearing flower-trimmed glasses">
    <span class="product-tag">NEW ARRIVAL</span>
  </div>
  <div class="abs product" style="left:679px;background:linear-gradient(#e8dcc8,#d8c2a4 55%,#e4d6c2)" role="img" aria-label="Photograph of the doll in a flowing floral gown"></div>
  <div class="abs product-name" style="left:166px">Cloud Drifter</div>
  <div class="abs product-name" style="left:337px">Cameo Pendant</div>
  <div class="abs product-name" style="left:508px;top:1017px">Petal Spectacles</div>
  <div class="abs product-name" style="left:679px">Bloom Parlour</div>

  <footer class="abs footer"></footer>
  <div class="abs footer-title">Get In Touch</div>
  <div class="abs social" style="left:452px;background:#4a6fb0" role="img" aria-label="Social page link"></div>
  <div class="abs social" style="left:483px;background:#5bb8e8" role="img" aria-label="Social feed link"></div>
  <svg class="abs social" style="left:514px" width="22" height="22" viewBox="0 0 22 22" aria-label="Email"><rect x="1" y="4" width="20" height="14" rx="1.5" fill="#f4f4f4" stroke="#9a9a9a"/><path d="M1.5 5 L11 12 L20.5 5" fill="none" stroke="#9a9a9a" stroke-width="1.2"/></svg>
</div>
</body>
</html>
```